International Company needs a Letterhead & Envelope Design

Our Company name is Corvale Brightwick Limited.
We'd like to ask the Designers for the luxurious and sophisticated design. Our logo is very simple and neat with letter logos, so we look forward to more professional and refined designs from Designers.
We look forward to providing you with a great design.
Thanks very much in advance.

```html
<!DOCTYPE html>
<html lang="en">
<head>
<meta charset="utf-8">
<title>Corvale Brightwick Limited — Letterhead &amp; Envelope</title>
<link rel="stylesheet" href="https://fonts.googleapis.com/css2?family=Open+Sans:wght@400;600;800&display=swap">
<style>
  :root {
    --backdrop: #c9c9c9;
    --paper: #ffffff;
    --ink: #111111;
    --body-text: #4a4a4a;
    --faint: #ececec;
    --signature-tone: #cfcfcf;
  }
  * { margin: 0; padding: 0; box-sizing: border-box; }
  html, body { width: 1200px; height: 1200px; overflow: hidden; }
  body {
    background: var(--backdrop);
    font-family: "Open Sans", Arial, sans-serif;
    position: relative;
    color: var(--ink);
  }
  .sheet {
    position: absolute;
    background: var(--paper);
    box-shadow: 0 2px 6px rgba(0,0,0,.25);
    overflow: hidden;
  }
  .abs { position: absolute; }

  /* Letterhead */
  .letterhead { left: 131px; top: 330px; width: 552px; height: 712px; }
  .edge-bar { left: 0; top: 0; height: 100%; }
  .brand-name {
    font-weight: 800;
    letter-spacing: 1px;
    white-space: nowrap;
    color: var(--ink);
    line-height: 1;
  }
  .letterhead .brand-name { left: 0; width: 100%; text-align: center; top: 350px; top: 21px; font-size: 16px; }
  .letter-text { left: 52px; width: 447px; font-size: 8.6px; line-height: 16px; color: var(--body-text); }
  .letter-text p { margin-bottom: 16px; text-align: justify; }
  .issue-date { top: 128px; }
  .recipient { top: 150px; line-height: 11px; }
  .salutation { top: 211px; }
  .body-copy { top: 242px; }
  .watermark {
    left: 0; width: 100%; top: 335px; text-align: center;
    font-size: 40px; font-weight: 800; color: var(--faint); letter-spacing: 2px;
  }
  .closing { top: 483px; }
  .signature { left: 52px; top: 506px; width: 128px; height: 16px; background: linear-gradient(90deg, var(--signature-tone), #e6e6e6); border-radius: 8px; }
  .signer { left: 52px; top: 529px; font-size: 10.5px; color: #222; }
  .signer-role { left: 52px; top: 548px; font-size: 8.6px; color: var(--body-text); }
  .footer-address { left: 0; width: 100%; text-align: center; top: 657px; font-size: 10px; color: #222; }
  .footer-rule { left: 52px; top: 674px; width: 454px; height: 1px; background: var(--ink); }
  .footer-contact { left: 0; width: 100%; text-align: center; top: 677px; font-size: 10px; color: #222; }
  .footer-contact b, .env-contact b { font-weight: 600; }

  /* Envelope front */
  .envelope-front { left: 736px; top: 599px; width: 408px; height: 205px; }
  .envelope-front .brand-name { left: 20px; top: 16px; font-size: 13px; }
  .env-contact { left: 23px; top: 164px; font-size: 7px; color: #222; white-space: nowrap; }
  .env-rule { left: 22px; top: 177px; width: 356px; height: 1px; background: var(--ink); }
  .env-address { left: 23px; top: 181px; font-size: 7px; color: #222; }

  /* Envelope back */
  .envelope-back { left: 736px; top: 839px; width: 408px; height: 203px; }
  .flap { left: 0; top: 0; }
  .envelope-back .brand-name { left: 0; width: 100%; text-align: center; top: 20px; font-size: 13px; color: var(--paper); }
</style>
</head>
<body>

  <section class="sheet letterhead">
    <svg class="abs edge-bar" width="14" height="712" viewBox="0 0 14 712">
      <rect x="0" y="0" width="10" height="712" fill="var(--ink)"/>
      <path d="M0 104 L12 112" stroke="#fff" stroke-width="2"/>
      <path d="M0 630 L12 638" stroke="#fff" stroke-width="2"/>
    </svg>
    <div class="abs brand-name">CORVALE BRIGHTWICK</div>

    <div class="abs watermark" aria-hidden="true">CORVALE</div>

    <div class="abs letter-text issue-date">Issuing Date: May 5, 2018</div>
    <div class="abs letter-text recipient">Name Of Employee Mr. XYZABC<br>Address of Employee<br>Address Line 2 etc..</div>
    <div class="abs letter-text salutation">Dear Mr.XYZABC</div>
    <div class="abs letter-text body-copy">
      <p>Lorem Ipsum has been the industry's standard dummy text ever since the 1500s, when an unknown printer took a galley of type and scrambled it to make a type specimen book. It has survived not only five centuries, but also the leap into electronic typesetting, remaining essentially unchanged. It was popularised in the 1960s with the release of Letraset sheets containing Lorem Ipsum passages, and more recently with desktop publishing software like Aldus PageMaker including versions of Lorem Ipsum.</p>
      <p>Lorem Ipsum is simply dummy text of the printing and typesetting industry. Lorem Ipsum has been the industry's standard dummy text ever since the 1500s, when an unknown printer took a galley of type and scrambled it to make a type specimen book.</p>
      <p>It has survived not only five centuries, but also the leap into electronic typesetting, remaining essentially unchanged. It was popularised in the 1960s with the release of Letraset sheets containing Lorem IpsumIpsum passages.</p>
    </div>
    <div class="abs letter-text closing">Yours Sincerely</div>
    <div class="abs signature" role="img" aria-label="Handwritten signature of Elias Marwood"></div>
    <div class="abs signer">Elias Marwood</div>
    <div class="abs signer-role">Managing Director</div>

    <div class="abs footer-address">421, Address line here 45452,Country Name</div>
    <div class="abs footer-rule"></div>
    <div class="abs footer-contact"><b>P:</b> 044-210 387 615 | <b>E:</b> info@corvalebrightwick.com | www.corvalebrightwick.com</div>
  </section>

  <section class="sheet envelope-front">
    <svg class="abs edge-bar" width="12" height="205" viewBox="0 0 12 205">
      <rect x="0" y="0" width="7" height="205" fill="var(--ink)"/>
      <path d="M0 14 L8 20" stroke="#fff" stroke-width="1.5"/>
      <path d="M0 178 L8 184" stroke="#fff" stroke-width="1.5"/>
    </svg>
    <div class="abs brand-name">CORVALE BRIGHTWICK</div>
    <div class="abs env-contact"><b>P:</b> 044-210 387 615 | <b>E:</b> info@corvalebrightwick.com | www.corvalebrightwick.com</div>
    <div class="abs env-rule"></div>
    <div class="abs env-address">421, Address line here 45452,Country Name</div>
  </section>

  <section class="sheet envelope-back">
    <svg class="abs flap" width="408" height="48" viewBox="0 0 408 48">
      <polygon points="0,0 408,0 392,48 16,48" fill="var(--ink)"/>
    </svg>
    <div class="abs brand-name">CORVALE BRIGHTWICK</div>
  </section>

</body>
</html>
```